ALL TEXT GRAPHICS TM May 2025 for Instagram

We are looking for a series of social media graphics for Instagram (new size: 4:5 (1080 x 1350 pixels) ratio that are ALL TEXT. We want the following quotes below on each graphic; one quote per graphic. AND, In very small letters at the bottom of each graphic, add @TovaMarshOnline
The look and feel of these graphics should be complimentary to the color palette attached below; but keep them simple. But the design is up to you; at the end of this document, I provided various samples of all text graphics that I like as examples.
Target Market(s)
women looking to lose weight
Look and feel

```html
<!DOCTYPE html>
<html lang="en">
<head>
<meta charset="utf-8">
<title>TM Instagram Text Graphics</title>
<link href="https://fonts.googleapis.com/css2?family=Poppins:wght@300;400;500;600;700&display=swap" rel="stylesheet">
<style>
:root{
  --page:#fdeef6;
  --white:#ffffff;
  --hot:#ff3399;
  --magenta:#cc0066;
  --mid:#e61a80;
  --blush:#ffcce4;
  --ink:#1a1a1a;
  --rule:#f2a0c8;
}
*{margin:0;padding:0;box-sizing:border-box}
html,body{width:781px;height:1200px;overflow:hidden;background:var(--page)}
body{position:relative;font-family:"Poppins",sans-serif}
.card{position:absolute;width:211px;height:264px;overflow:hidden}
.col-1{left:64.5px}.col-2{left:285px}.col-3{left:505px}
.row-1{top:53px}.row-2{top:330px}.row-3{top:607px}.row-4{top:884px}
.bg-white{background:var(--white)}
.bg-hot{background:var(--hot)}
.bg-magenta{background:var(--magenta)}
.bg-fade{background:linear-gradient(180deg,#ee2a8c 0%,#e0167c 60%,#d00c6e 100%)}
.block{position:absolute;left:0;right:0;text-align:center;font-weight:300;letter-spacing:-0.01em}
.lead{font-size:9px;line-height:11px;font-weight:400}
.handle{position:absolute;left:0;right:0;text-align:center;font-size:6px;line-height:8px;font-weight:500;letter-spacing:0.16em}
.ring{position:absolute;border-radius:50%;border-style:solid}
.disc{position:absolute;border-radius:50%}
.rule-v{position:absolute;width:1px}
.dot{position:absolute;width:3px;height:3px;border-radius:50%}
b{font-weight:600}
</style>
</head>
<body>

<!-- Card 1 -->
<section class="card col-1 row-1 bg-white">
  <div class="ring" style="width:98px;height:98px;left:162px;top:-49px;border-width:30px;border-color:var(--blush)"></div>
  <div class="ring" style="width:58px;height:58px;left:-29px;top:235px;border-width:19px;border-color:var(--hot)"></div>
  <p class="block lead" style="top:58px;color:var(--ink)">Tired. Moody. Stubborn Belly Fat.</p>
  <p class="block" style="top:81px;font-size:22.5px;line-height:23.5px;color:#f03c96">Your hormones<br>are screaming<br>for help!</p>
  <p class="block" style="top:167px;font-size:31px;line-height:34px;color:var(--magenta)">Let’s fix that.</p>
  <span class="rule-v" style="left:105px;top:210px;height:27px;background:var(--rule)"></span>
  <span class="dot" style="left:104px;top:235px;background:var(--magenta)"></span>
  <p class="handle" style="top:241px;color:var(--ink)">@TovaMarshOnline</p>
</section>

<!-- Card 2 -->
<section class="card col-2 row-1 bg-hot">
  <div class="disc" style="width:58px;height:58px;left:182px;top:-29px;background:var(--blush)"></div>
  <p class="block lead" style="top:61px;left:14px;text-align:left;color:var(--white)">That stubborn weight?</p>
  <p class="block" style="top:82px;left:14px;text-align:left;font-size:23px;line-height:21.5px;color:var(--white)">It’s not<br>your fault.</p>
  <p class="block" style="top:139px;left:14px;text-align:left;font-size:16px;line-height:15.7px;color:var(--white)">Your hormones are<br>to blame and<br>you’re not alone;<br>But there is a fix.</p>
  <span style="position:absolute;left:0;top:245px;width:127px;height:1px;background:#8a1f52"></span>
  <span class="dot" style="left:126px;top:244px;background:var(--ink)"></span>
  <p class="handle" style="top:241px;left:132px;right:auto;text-align:left;color:var(--white)">@TovaMarshOnline</p>
</section>

<!-- Card 3 -->
<section class="card col-3 row-1 bg-magenta">
  <svg style="position:absolute;left:88px;top:15px" width="35" height="43" viewBox="0 0 35 43" aria-hidden="true">
    <polygon points="0,0 35,0 17.5,12" fill="#e0609f"/>
    <polygon points="0,15 35,15 17.5,27" fill="#ee94c2"/>
    <polygon points="0,30 35,30 17.5,42" fill="var(--blush)"/>
  </svg>
  <div class="ring" style="width:116px;height:116px;left:47.5px;top:206px;border-width:13px;border-color:var(--mid)"></div>
  <span class="rule-v" style="left:105px;top:218px;height:17px;background:#e0408f"></span>
  <span class="dot" style="left:104px;top:234px;background:#e0408f"></span>
  <p class="block lead" style="top:73px;color:var(--blush)">Your belly isn’t fat… it’s hormonal.</p>
  <p class="block" style="top:96px;font-size:25px;line-height:24px;color:var(--white)">And here’s how<br>to fix it.</p>
  <p class="block" style="top:157px;font-size:16px;line-height:16px;color:var(--white)">Comment <b>HORMONES</b><br>if nothing is working.</p>
  <p class="handle" style="top:241px;color:var(--white)">@TovaMarshOnline</p>
</section>

<!-- Card 4 -->
<section class="card col-1 row-2 bg-white">
  <div style="position:absolute;left:14px;top:14px;width:182px;height:231px;border:1px solid var(--rule);border-bottom:none"></div>
  <span style="position:absolute;left:14px;top:244px;width:112px;height:1px;background:var(--rule)"></span>
  <span class="dot" style="left:125px;top:243px;background:var(--magenta)"></span>
  <p class="block lead" style="top:77px;color:var(--ink)">The stubborn belly fat after 40?</p>
  <p class="block" style="top:98px;right:25px;text-align:right;font-size:16px;line-height:16px;color:var(--hot)">It’s not about<br>calories; it’s about<br>your hormones.</p>
  <p class="block" style="top:157px;font-size:24px;line-height:28px;color:var(--magenta)">Here is the fix!</p>
  <p class="handle" style="top:241px;left:132px;right:auto;text-align:left;color:var(--ink)">@TovaMarshOnline</p>
</section>

<!-- Card 5 -->
<section class="card col-2 row-2 bg-magenta">
  <div class="ring" style="width:98px;height:98px;left:162px;top:-49px;border-width:30px;border-color:var(--mid)"></div>
  <div style="position:absolute;left:0;top:235px;width:211px;height:19px;background:var(--white)"></div>
  <div class="ring" style="width:58px;height:58px;left:-29px;top:235px;border-width:19px;border-color:var(--blush)"></div>
  <p class="block lead" style="top:77px;color:var(--blush)">Flat tummy in your 40s?</p>
  <p class="block" style="top:98px;font-size:25px;line-height:28px;color:var(--white)">It’s still possible!</p>
  <p class="block" style="top:137px;font-size:16px;line-height:15.5px;color:var(--blush)">Comment <b>BYE BELLY</b><br>to get the 10 secrets<br>to a flatter tummy</p>
  <p class="handle" style="top:240px;color:var(--ink)">@TovaMarshOnline</p>
</section>

<!-- Card 6 -->
<section class="card col-3 row-2 bg-hot">
  <div style="position:absolute;left:10px;top:10px;width:191px;height:244px;border:1px solid #d6006b"></div>
  <span class="rule-v" style="left:105px;top:10px;height:38px;background:#d6006b"></span>
  <div style="position:absolute;left:10px;top:239px;width:191px;height:15px;background:var(--magenta)"></div>
  <p class="block lead" style="top:62px;line-height:14px;font-weight:500;color:var(--white)">Bloating.<br>Muffin top.<br>Puffy waistline.</p>
  <p class="block" style="top:112px;font-size:16px;line-height:16px;color:var(--white)">Your body’s<br>screaming for a<br>different kind of fix.</p>
  <p class="block" style="top:171px;font-size:24px;line-height:28px;color:var(--white)">Here it is.</p>
  <p class="handle" style="top:242px;color:var(--white)">@TovaMarshOnline</p>
</section>

<!-- Card 7 -->
<section class="card col-1 row-3 bg-white">
  <div style="position:absolute;left:0;top:0;width:211px;height:10px;background:var(--blush)"></div>
  <p class="block" style="top:56px;font-size:16.5px;line-height:19.6px;color:var(--hot)">You’re doing all the<br>“<b>right</b>” things, but your<br>belly won’t go down?</p>
  <p class="block" style="top:126px;font-size:25px;line-height:23px;color:var(--magenta)">Here’s what you<br>haven’t tried.</p>
  <p class="handle" style="top:222px;color:var(--ink)">@TovaMarshOnline</p>
  <span class="rule-v" style="left:105px;top:240px;height:24px;background:#555"></span>
</section>

<!-- Card 8 -->
<section class="card col-2 row-3 bg-fade">
  <div style="position:absolute;left:0;top:0;width:211px;height:10px;background:var(--magenta)"></div>
  <div class="ring" style="width:116px;height:116px;left:-58px;top:206px;border-width:13px;border-color:var(--blush)"></div>
  <div class="ring" style="width:116px;height:116px;left:153px;top:206px;border-width:13px;border-color:var(--blush)"></div>
  <div class="ring" style="width:95px;height:95px;left:58px;top:240px;border-width:12px;border-color:var(--hot)"></div>
  <p class="block" style="top:48px;font-size:16.5px;line-height:19.5px;color:var(--white)">This 90-day plan<br>helped women over 40<br>slim down, get<br>a tiny waist and feel<br>sexy again.</p>
  <p class="block" style="top:155px;font-size:25px;line-height:28px;color:var(--white)">You’re next.</p>
  <p class="handle" style="top:222px;color:var(--white)">@TovaMarshOnline</p>
</section>

<!-- Card 9 -->
<section class="card col-3 row-3 bg-magenta">
  <div class="ring" style="width:98px;height:98px;left:-49px;top:-49px;border-width:30px;border-color:var(--mid)"></div>
  <div style="position:absolute;left:0;top:233px;width:211px;height:19px;background:var(--hot)"></div>
  <div class="ring" style="width:58px;height:58px;left:182px;top:235px;border-width:19px;border-color:var(--blush)"></div>
  <p class="block" style="top:42px;font-size:16.5px;line-height:15.7px;color:var(--blush)">This is the secret<br>women over 40 are<br>using to get<br>snatched; without<br>starving.</p>
  <p class="block" style="top:133px;font-size:21px;line-height:19.5px;color:var(--white)">Comment<br><b>SKINNY</b> to get<br>the exact plan.</p>
  <p class="handle" style="top:238.5px;color:var(--white)">@TovaMarshOnline</p>
</section>

<!-- Card 10 -->
<section class="card col-2 row-4 bg-white">
  <p class="block" style="top:30px;left:26px;text-align:left;font-size:16.5px;line-height:16px;color:var(--hot)">What worked in your<br>30s won’t work now.</p>
  <p class="block" style="top:77px;left:26px;text-align:left;font-size:24px;line-height:23px;color:var(--magenta)">Here’s what<br>actually<br>does. Drop 30<br>Pounds in 3<br>Months.</p>
  <svg style="position:absolute;left:26px;top:224px" width="161" height="29" viewBox="0 0 161 29" aria-hidden="true">
    <polygon points="0,7 27,0 27,7" fill="var(--hot)"/>
    <polygon points="134,23 160,23 134,29" fill="var(--hot)"/>
    <rect x="0" y="7" width="160" height="16" fill="var(--magenta)"/>
  </svg>
  <p class="handle" style="top:235px;color:var(--white)">@TovaMarshOnline</p>
</section>

</body>
</html>
```